Marcus Fenwick Consulting Webpage

I need to transition into a Wordpress website to be able to insert tracking code. This was a HostVerra website, but now I'm limited on functionality

Here are requirements: I need to replicate marcusfenwick.example

My company is focused in search and placement, consulting and workforce development for the turfgrass and hospitality industry

I'm also looking to integrate the following for a recruiting agency job board.
Multiple Dashboard view
✔ Job map
✔ Demo Content upload
✔ Chat button
✔ CV/Resume builder
✔ Featured job on top
✔ Email Alert
✔ Job bookmark
✔ Job CV package
✔ Social media Login
✔ SEO set up
✔ Plugin installation
✔ Featured jobs
✔ Payment gateway integration and set up
✔ Responsive design

Target Market(s)

Golf and turfgrass businesses; as well as candidates for those companies

Industry/Entity Type

Turfgrass and Golf Industry

Coding

Coded - Design and coding required

Font styles to use
Sans Serif

Colors

Designer to choose colors to be used in the design.

Requirements
Must have
• Functionality of HostVerra Web Design builder, Chat box capability, pop up capability, scheduling/appointment booking integration, ability to upload videos similar to my current website, e-commerce capabilities
Nice to have
• Everything to integrate "recruiting agency" aspect to collect information from potential candidates

```html
<!DOCTYPE html>
<html lang="en">
<head>
<meta charset="utf-8">
<title>Marcus Fenwick Consulting</title>
<link href="https://fonts.googleapis.com/css2?family=Oswald:wght@400;500;600;700&family=Open+Sans:wght@400;600;700&display=swap" rel="stylesheet">
<style>
:root{
  --green:#4a5b4d;
  --green-dark:#3c4a3f;
  --ink:#2b2f2c;
  --muted:#6d726e;
  --line:#e3e5e3;
  --paper:#ffffff;
  --mist:#f3f4f3;
  --outline:#d9dcd9;
  --gold:#e0a92b;
}
*{margin:0;padding:0;box-sizing:border-box}
html,body{width:1200px;height:4820px;overflow:hidden}
body{position:relative;background:var(--paper);font-family:"Open Sans",Arial,sans-serif;color:var(--ink)}
.heading{font-family:"Oswald",Arial,sans-serif;font-weight:600;text-transform:uppercase;color:var(--green-dark)}
.section-title{position:absolute;left:0;width:1200px;text-align:center;font-size:46px;letter-spacing:.5px;line-height:1.2}
.ghost-word{position:absolute;font-family:"Oswald",Arial,sans-serif;font-weight:700;text-transform:uppercase;color:transparent;-webkit-text-stroke:1.5px var(--outline);letter-spacing:6px;line-height:1;white-space:nowrap}
.photo{position:absolute}

/* hero */
.hero{position:absolute;left:0;top:0;width:1200px;height:820px;background:var(--green)}
.brand{position:absolute;left:80px;top:34px;display:flex;align-items:center;gap:14px;color:#fff;font-family:"Oswald",Arial,sans-serif;font-weight:600;font-size:26px;text-transform:uppercase;line-height:1.05;white-space:nowrap}
.brand .mark{width:22px;height:22px;border:2px solid #fff;border-radius:50%}
.brand small{display:block;font-size:13px;letter-spacing:4px;font-weight:400}
.nav{position:absolute;left:430px;top:56px;display:flex;gap:22px;align-items:center;font-size:12px;font-weight:700;color:#fff;text-transform:uppercase;letter-spacing:.4px;white-space:nowrap}
.hero-title{position:absolute;left:80px;top:150px;font-size:64px;line-height:1.12;color:#fff;font-family:"Oswald",Arial,sans-serif;font-weight:600;text-transform:uppercase}
.hero-lead{position:absolute;left:770px;top:190px;width:260px;color:#e6ebe6;font-size:15px;line-height:1.6}
.btn{display:inline-block;background:var(--green-dark);color:#fff;font-size:12px;font-weight:700;text-transform:uppercase;letter-spacing:1px;padding:13px 24px}
.hero .btn{position:absolute;left:770px;top:264px;background:#3a463c}

.about-text{position:absolute;left:190px;top:1270px;width:820px;text-align:center;font-size:15px;line-height:2;text-transform:uppercase;color:var(--muted);letter-spacing:.4px}
.rule{position:absolute;left:100px;width:1000px;height:1px;background:var(--line)}

/* services */
.service{position:absolute;top:1520px;width:320px;height:470px;background:#fff;box-shadow:0 6px 24px rgba(0,0,0,.12)}
.service .photo{left:0;top:0;width:320px;height:200px}
.service h3{position:absolute;left:24px;top:228px;font-size:16px;color:var(--ink);font-weight:700;text-transform:uppercase;white-space:nowrap}
.service p{position:absolute;left:24px;top:262px;width:272px;font-size:14px;line-height:1.6;color:var(--muted)}
.arrow-btn{position:absolute;right:24px;bottom:24px;width:32px;height:32px;background:var(--green-dark);display:flex;align-items:center;justify-content:center}

/* testimonials */
.quote{position:absolute;top:2950px;width:380px;height:200px;display:flex;gap:20px}
.quote .badge{flex:none;width:90px;height:90px;background:var(--mist);display:flex;align-items:center;justify-content:center}
.quote .badge span{width:54px;height:54px;background:#b8c2b0}
.quote h4{font-size:12px;font-weight:700;text-transform:uppercase;color:var(--ink);margin-top:4px}
.quote p{font-size:13px;line-height:1.55;color:var(--muted);margin-top:10px;width:250px}
.quote .meta{display:flex;justify-content:space-between;width:250px;margin-top:18px;font-size:11px;font-weight:700;text-transform:uppercase;color:var(--muted)}
.stars{color:var(--gold);letter-spacing:2px}

/* news */
.news-band{position:absolute;left:0;top:3540px;width:1200px;height:300px;background:var(--mist)}
.news{position:absolute;top:3360px;width:390px;height:360px;background:#fff;box-shadow:0 6px 24px rgba(0,0,0,.1)}
.news .photo{left:0;top:0;width:390px;height:195px}
.news .date{position:absolute;left:24px;top:210px;font-size:11px;color:var(--muted)}
.news h3{position:absolute;left:24px;top:232px;width:340px;font-family:"Oswald",Arial,sans-serif;font-weight:600;font-size:19px;line-height:1.2;text-transform:uppercase;color:var(--ink)}
.news p{position:absolute;left:24px;top:292px;width:340px;font-size:13px;line-height:1.55;color:var(--muted)}

/* partners */
.partners{position:absolute;left:170px;top:4165px;width:860px;display:flex;justify-content:space-between}
.partners span{width:78px;height:78px;border-radius:50%;background:#d8ddd6}
.partners span:nth-child(odd){background:#c7d0c9}

/* footer */
.footer{position:absolute;left:0;top:4270px;width:1200px;height:550px;background:var(--green);color:#fff}
.footer-brand{position:absolute;left:100px;top:200px;width:260px;text-align:center;font-family:"Oswald",Arial,sans-serif;font-weight:600;font-size:30px;text-transform:uppercase;line-height:1.1}
.footer-brand small{display:block;font-size:14px;letter-spacing:6px;font-weight:400;margin-top:6px}
.footer h5{font-family:"Oswald",Arial,sans-serif;font-size:18px;font-weight:600;text-transform:uppercase;letter-spacing:.5px}
.contact-info{position:absolute;left:420px;top:52px;width:300px}
.contact-info li{list-style:none;display:flex;gap:12px;margin-top:20px;font-size:13px;line-height:1.5}
.contact-info b{display:block;font-size:11px;text-transform:uppercase}
.socials{display:flex;gap:10px;margin-top:28px}
.socials span{width:34px;height:34px;border:1px solid rgba(255,255,255,.5)}
.form{position:absolute;left:740px;top:52px;width:360px}
.form .row{display:flex;gap:14px;margin-top:16px}
.form label{display:block;font-size:11px;font-weight:700;margin-bottom:6px}
.form .field{background:#fff;height:34px;color:#9aa09b;font-size:12px;padding:9px 12px}
.form .send{margin-top:14px;background:#fff;color:var(--green-dark);text-align:center;font-size:13px;font-weight:700;padding:10px}
.bottom-bar{position:absolute;left:0;top:500px;width:1200px;height:50px;background:var(--green-dark);display:flex;align-items:center;justify-content:space-between;padding:0 40px;font-size:11px;font-weight:700;text-transform:uppercase;letter-spacing:.5px}
.bottom-bar nav{display:flex;gap:28px}
</style>
</head>
<body>

<header class="hero">
  <div class="brand"><span class="mark"></span><div>Marcus Fenwick<small>Consulting</small></div></div>
  <nav class="nav">
    <span>Home</span><span>Marcus Fenwick</span><span>Services</span><span>Latest News</span><span>Recent Clients</span><span>Contact</span>
    <svg width="14" height="14" viewBox="0 0 14 14" fill="#fff"><circle cx="7" cy="4" r="3.2"/><path d="M1 14c0-3.5 2.7-5.5 6-5.5s6 2 6 5.5z"/></svg>
    <span style="display:flex;gap:6px;align-items:center"><svg width="16" height="14" viewBox="0 0 16 14" fill="none" stroke="#fff" stroke-width="1.5"><path d="M1 1h3l2 8h8l1.5-6H5"/><circle cx="7" cy="12" r="1"/><circle cx="13" cy="12" r="1"/></svg>$0.00</span>
  </nav>
  <h1 class="hero-title">We Create<br>Sustainable Talent<br>Solutions</h1>
  <p class="hero-lead">Marcus's passion for the game of golf began at the age of 9.</p>
  <span class="btn">Get Started</span>
</header>

<div class="photo" role="img" aria-label="Golf course at sunset with sand bunkers and green fairway" style="left:160px;top:508px;width:680px;height:400px;background:linear-gradient(180deg,#d9b98a 0%,#a7a783 38%,#5f7a45 60%,#d8cfae 78%,#4e6b38 100%)"></div>
<div class="photo" role="img" aria-label="Consultant meeting with a client in a bright office" style="left:840px;top:440px;width:268px;height:300px;background:linear-gradient(160deg,#e9ecef,#b9c0c6 60%,#8c959c);box-shadow:0 6px 20px rgba(0,0,0,.2)"></div>
<div class="photo" role="img" aria-label="Empty meeting room with chairs" style="left:88px;top:820px;width:264px;height:220px;background:linear-gradient(180deg,#eceeee,#c9ccca 60%,#9a9d99);box-shadow:0 6px 20px rgba(0,0,0,.15)"></div>

<div class="ghost-word" style="left:410px;top:950px;font-size:210px">About</div>
<p class="about-text">Marcus's passion for the game of golf began at the age of 9. After playing high school golf, Marcus attended Northfield State University to study Turfgrass Science. An intimate of three top 100 golf courses - Harrow Ridge Golf Club, Stonebrook Hills Country Club for the 2007 National Championship and Fairhaven Village Golf Club for the 2009 Lakeview Invitational.</p>
<div class="rule" style="top:1420px"></div>

<h2 class="heading section-title" style="top:1432px">How We Help You</h2>

<article class="service" style="left:112px">
  <div class="photo" role="img" aria-label="Modern conference room with chairs and long table" style="background:linear-gradient(180deg,#cfc9bf,#8e8576 70%,#6c5f50)"></div>
  <h3>Search and Placement</h3>
  <p>Powered by our national presence, unmatched recruiting network and deep search process.</p>
  <span class="arrow-btn"><svg width="10" height="10" viewBox="0 0 10 10" fill="#fff"><path d="M3 1l5 4-5 4z"/></svg></span>
</article>
<article class="service" style="left:440px">
  <div class="photo" role="img" aria-label="Golf green with bunker and trees" style="background:linear-gradient(180deg,#c8d6df,#6f8f55 55%,#d9cfa8 75%,#4f7236)"></div>
  <h3>Workforce Development</h3>
  <p>Our customized partnership models allow us to be responsive to your unique needs.</p>
  <span class="arrow-btn"><svg width="10" height="10" viewBox="0 0 10 10" fill="#fff"><path d="M3 1l5 4-5 4z"/></svg></span>
</article>
<article class="service" style="left:772px">
  <div class="photo" role="img" aria-label="Audience seated at a consulting seminar" style="background:linear-gradient(180deg,#b08a62,#6e5644 60%,#3e3330)"></div>
  <h3>Marcus Fenwick Consulting</h3>
  <p>Marcus utilizes a proven framework backed by 15+ years of data and science to help business.</p>
  <span class="arrow-btn"><svg width="10" height="10" viewBox="0 0 10 10" fill="#fff"><path d="M3 1l5 4-5 4z"/></svg></span>
</article>

<div class="photo" role="img" aria-label="Golf course fairway with trees" style="left:0;top:2120px;width:136px;height:540px;background:linear-gradient(180deg,#b7c7a4,#5f7f44 60%,#3e5a2b)"></div>
<div class="photo" role="img" aria-label="Open plan office with wooden desks and bright windows" style="left:148px;top:2008px;width:900px;height:652px;background:linear-gradient(180deg,#f1f1ef 0%,#d9dad6 45%,#c9b79a 75%,#a99478 100%)"></div>
<div class="photo" role="img" aria-label="Team working together at a table" style="left:1060px;top:2120px;width:140px;height:540px;background:linear-gradient(180deg,#8a6b4f,#c6a484 50%,#5b4a3d)"></div>
<div class="ghost-word" style="left:80px;top:2600px;font-size:160px;opacity:.8">Projects</div>

<h2 class="heading section-title" style="top:2830px">Testimonials</h2>

<div class="quote" style="left:100px">
  <div class="badge"><span></span></div>
  <div><h4>Head Golf Professional</h4><p>The quality and value the team gets from Marcus is off the charts, highly recommended!</p><div class="meta"><span>Read More</span><span class="stars">★★★★★</span></div></div>
</div>
<div class="quote" style="left:460px">
  <div class="badge"><span></span></div>
  <div><h4>Director of Landscape</h4><p>Without question, Marcus has helped the team with dozens of qualified applicants for us.</p><div class="meta"><span>Read More</span><span class="stars">★★★★★</span></div></div>
</div>
<div class="quote" style="left:930px">
  <div class="badge"><span></span></div>
  <div><h4>General Manager</h4><p>Thank you so much for the search and placement process, a pleasure to work with.</p><div class="meta"><span>Read More</span><span class="stars">★★★★★</span></div></div>
</div>

<div class="rule" style="top:3190px"></div>
<h2 class="heading section-title" style="top:3260px">Latest News</h2>

<div class="news-band"></div>
<div class="ghost-word" style="left:120px;top:3650px;font-size:170px">Articles</div>

<article class="news" style="left:200px">
  <div class="photo" role="img" aria-label="Golf course with sand bunkers under a blue sky" style="background:linear-gradient(180deg,#8fb6da,#6f9a53 50%,#ddd1a8 72%,#4f7634)"></div>
  <span class="date">By admin · January 2022</span>
  <h3>New Talent Helps Restore Willow Crest Hunt Club</h3>
  <p>Brookmere Falls - When Willow Crest Hunt Club underwent a grand course restoration.</p>
</article>
<article class="news" style="left:612px">
  <div class="photo" role="img" aria-label="Golfer in a sun hat on the course" style="background:linear-gradient(180deg,#9fc0e0,#c9d6e4 40%,#6f9a55 75%,#4e7336)"></div>
  <span class="date">By admin · January 2022</span>
  <h3>Golf Course Industry Firm &amp; Fast</h3>
  <p>You may like fast to follow trends in hiring and recruiting? Marcus shares insights.</p>
</article>

<h2 class="heading section-title" style="top:4080px">Our Partners</h2>
<div class="partners"><span></span><span></span><span></span><span></span><span></span><span></span><span></span></div>

<footer class="footer">
  <div class="footer-brand">Marcus Fenwick<small>Consulting</small></div>
  <div class="contact-info">
    <h5>Contact Info</h5>
    <ul>
      <li><svg width="14" height="18" viewBox="0 0 14 18" fill="#fff"><path d="M7 0a7 7 0 0 0-7 7c0 5 7 11 7 11s7-6 7-11a7 7 0 0 0-7-7zm0 10a3 3 0 1 1 0-6 3 3 0 0 1 0 6z"/></svg><div><b>Location</b>22 Laurel Drive, Elmhaven,<br>Pennsylvania 17800, United States</div></li>
      <li><svg width="14" height="14" viewBox="0 0 14 14" fill="#fff"><path d="M3 0l2.5 3.5-1.5 2a8 8 0 0 0 4.5 4.5l2-1.5L14 11l-1.5 3C6 14 0 8 0 1.5z"/></svg><div><b>Phone</b>570-555-0142</div></li>
      <li><svg width="16" height="12" viewBox="0 0 16 12" fill="none" stroke="#fff" stroke-width="1.4"><rect x=".7" y=".7" width="14.6" height="10.6"/><path d="M1 1l7 6 7-6"/></svg><div><b>Email</b>mfenwick.golf@example.com</div></li>
    </ul>
    <div class="socials"><span></span><span></span><span></span><span></span></div>
  </div>
  <div class="form">
    <h5>Contact Form</h5>
    <div class="row">
      <div style="flex:1"><label>Name*</label><div class="field">Enter your name</div></div>
      <div style="flex:1"><label>Email*</label><div class="field">Enter your email</div></div>
    </div>
    <div style="margin-top:16px"><label>Phone*</label><div class="field">Enter phone number</div></div>
    <div style="margin-top:16px"><label>Message*</label><div class="field" style="height:90px">Type your text</div></div>
    <div class="send">Send</div>
  </div>
  <div class="bottom-bar">
    <span>Copyright © 2022 MFENWICK, LLC – All Rights Reserved.</span>
    <nav><span>Appointments</span><span>Careers</span><span>Programs</span></nav>
  </div>
</footer>

</body>
</html>
```